Clinique VitaMira business card

I am looking for a talented designer who can an existing design and make it better. I need a 2 sided business card to represent our Psychology clinic staff members. It would need to be elegant, yet modern, clean, light and uplifting. Simple design, quick turnaround time. Lots of files and logos to use as your guide. I hope to hear from you!

Target Market(s)

Clients who receive the card of our therapists

Industry/Entity Type

Health And Wellness

Contact Information for Business Card

Following the similar designs of the Bluepine Care Center card, there will be 2 sides. Side 1 (front) should have the vitamira logo instead of the bluepine care logo, The title should read Clinique VitaMira instead of centre Soins Pinbleu/Bluepine care Center.

Side 2 should have a spiral similar to the one on the card with sunflower leaves, and the title of the Therapist should be Marie Lise Benkirane, Psychologue, Psychologist, her email: Marie@Vitamira-example.com and phone number should be (514) 555-0173

Font styles to use
Serif

Colors
fee18a
85cae6
ffffff
0255a3

Requirements
Must have
• Side 1 (front): vitamira logo- Name of the clinic, clinic address, contact info of clinic etc. use little icons in front of each (just like on sample card)
side 2: Therapist name titles and their contact info underneath with design of spiral and/or sunflower leaves..
Nice to have
• soft colors along soft yellow/gold and blue like the logo,
mini icons for phone, email, address etc.
We do work with a holistic, zen approach so it should represent that to some extent

```html
<!DOCTYPE html>
<html lang="fr">
<head>
<meta charset="utf-8">
<title>Clinique VitaMira – cartes professionnelles</title>
<link href="https://fonts.googleapis.com/css2?family=Arimo:wght@400;700&display=swap" rel="stylesheet">
<style>
  :root {
    --backdrop: #2b2b2d;
    --navy: #29226a;
    --ink: #2a2470;
    --sun: #fdd21f;
    --amber: #f5a01c;
    --paper: #ffffff;
    --rule-gold: #8a7a3a;
    --rule-lilac: #b9b5dc;
    --text-dark: #222222;
  }
  * { box-sizing: border-box; margin: 0; padding: 0; }
  html, body {
    width: 1200px; height: 1015px; overflow: hidden;
    background: var(--backdrop);
    font-family: "Arimo", Arial, sans-serif;
  }
  .stage { position: relative; width: 1200px; height: 1015px; }
  .card {
    position: absolute; width: 640px; height: 366px;
    box-shadow: 0 10px 30px rgba(0,0,0,.45);
    overflow: hidden;
  }

  /* Therapist side */
  .card--therapist { left: 90px; top: 90px; background: var(--navy); }
  .sunflower-art {
    position: absolute; left: 30px; top: 28px; width: 310px; height: 310px;
    border-radius: 50%;
    background: radial-gradient(circle, var(--amber) 0%, var(--amber) 30%, var(--sun) 34%, var(--sun) 62%, rgba(253,210,31,0) 72%);
  }
  .card--therapist .divider {
    position: absolute; left: 362px; top: 120px; width: 1px; height: 130px;
    background: var(--rule-gold);
  }
  .therapist-info { position: absolute; left: 385px; top: 128px; width: 240px; color: var(--paper); }
  .therapist-name { color: var(--sun); font-weight: 700; font-size: 23px; line-height: 1.1; white-space: nowrap; }
  .therapist-title { font-size: 15px; margin-top: 4px; letter-spacing: .2px; }
  .contact-list { list-style: none; margin-top: 24px; font-size: 15px; }
  .contact-list li { display: flex; align-items: center; gap: 9px; margin-bottom: 6px; white-space: nowrap; }
  .icon { width: 15px; height: 15px; flex: none; }
  .card--therapist .icon { fill: var(--sun); }

  /* Clinic side */
  .card--clinic { left: 470px; top: 540px; background: var(--paper); }
  .brand {
    position: absolute; left: 48px; top: 150px;
    display: flex; align-items: center; gap: 12px;
  }
  .brand-dot { width: 34px; height: 34px; border-radius: 50%; background: var(--sun); }
  .brand-name { font-size: 40px; font-weight: 700; color: var(--ink); }
  .card--clinic .divider {
    position: absolute; left: 320px; top: 95px; width: 1px; height: 205px;
    background: var(--rule-lilac);
  }
  .clinic-info { position: absolute; left: 345px; top: 92px; width: 280px; color: var(--text-dark); }
  .clinic-name { color: var(--ink); font-weight: 700; font-size: 24px; white-space: nowrap; }
  .clinic-info .contact-list { margin-top: 10px; font-size: 14.5px; }
  .clinic-info .contact-list li { align-items: flex-start; margin-bottom: 3px; }
  .clinic-info .contact-list li.address { margin-bottom: 12px; line-height: 1.2; }
  .card--clinic .icon { fill: var(--ink); margin-top: 1px; }
  .social-square { width: 15px; height: 15px; background: var(--ink); border-radius: 2px; flex: none; margin-top: 1px; }
</style>
</head>
<body>
<main class="stage">

  <section class="card card--therapist" aria-label="Carte du thérapeute">
    <div class="sunflower-art" role="img" aria-label="Tournesol stylisé aux pétales jaunes avec une spirale orange au centre"></div>
    <div class="divider"></div>
    <div class="therapist-info">
      <h1 class="therapist-name">Marie Lise Benkirane</h1>
      <p class="therapist-title">Psychologue, Psychologist</p>
      <ul class="contact-list">
        <li>
          <svg class="icon" viewBox="0 0 24 24" aria-hidden="true"><path d="M6.6 10.8a15 15 0 0 0 6.6 6.6l2.2-2.2c.3-.3.7-.4 1-.2 1.1.4 2.3.6 3.6.6.6 0 1 .4 1 1V20c0 .6-.4 1-1 1A17 17 0 0 1 3 4c0-.6.4-1 1-1h3.5c.6 0 1 .4 1 1 0 1.3.2 2.5.6 3.6.1.3 0 .7-.2 1z"/></svg>
          (514) 555-0173
        </li>
        <li>
          <svg class="icon" viewBox="0 0 24 24" aria-hidden="true"><path d="M2 5h20v14H2zM4 7v.5l8 5 8-5V7l-8 5z"/></svg>
          Marie@Vitamira-example.com
        </li>
      </ul>
    </div>
  </section>

  <section class="card card--clinic" aria-label="Carte de la clinique">
    <div class="brand">
      <span class="brand-dot" aria-hidden="true"></span>
      <span class="brand-name">VitaMira</span>
    </div>
    <div class="divider"></div>
    <div class="clinic-info">
      <h2 class="clinic-name">Clinique VitaMira</h2>
      <ul class="contact-list">
        <li class="address">
          <svg class="icon" viewBox="0 0 24 24" aria-hidden="true"><path d="M12 2a7 7 0 0 0-7 7c0 5 7 13 7 13s7-8 7-13a7 7 0 0 0-7-7zm0 9.5A2.5 2.5 0 1 1 12 6.5a2.5 2.5 0 0 1 0 5z"/></svg>
          <span>4810 boul. des Érables ouest,<br>Lavalière, Qc., H0H 0A0</span>
        </li>
        <li>
          <svg class="icon" viewBox="0 0 24 24" aria-hidden="true"><path d="M6.6 10.8a15 15 0 0 0 6.6 6.6l2.2-2.2c.3-.3.7-.4 1-.2 1.1.4 2.3.6 3.6.6.6 0 1 .4 1 1V20c0 .6-.4 1-1 1A17 17 0 0 1 3 4c0-.6.4-1 1-1h3.5c.6 0 1 .4 1 1 0 1.3.2 2.5.6 3.6.1.3 0 .7-.2 1z"/></svg>
          514- 555-0173
        </li>
        <li>
          <svg class="icon" viewBox="0 0 24 24" aria-hidden="true"><path d="M2 5h20v14H2zM4 7v.5l8 5 8-5V7l-8 5z"/></svg>
          info@vitamira-example.com
        </li>
        <li>
          <svg class="icon" viewBox="0 0 24 24" aria-hidden="true"><path d="M12 2a10 10 0 1 0 0 20 10 10 0 0 0 0-20zm6.9 6h-3a15 15 0 0 0-1.3-3.9A8 8 0 0 1 18.9 8zM12 4c.8 1.2 1.5 2.5 1.9 4h-3.8c.4-1.5 1.1-2.8 1.9-4zM4.3 14a8 8 0 0 1 0-4h3.4a16 16 0 0 0 0 4zm.8 2h3a15 15 0 0 0 1.3 3.9A8 8 0 0 1 5.1 16zm3-8h-3a8 8 0 0 1 4.3-3.9A15 15 0 0 0 8.1 8zM12 20c-.8-1.2-1.5-2.5-1.9-4h3.8c-.4 1.5-1.1 2.8-1.9 4zm2.3-6H9.7a14 14 0 0 1 0-4h4.6a14 14 0 0 1 0 4zm.3 5.9a15 15 0 0 0 1.3-3.9h3a8 8 0 0 1-4.3 3.9zm1.7-5.9a16 16 0 0 0 0-4h3.4a8 8 0 0 1 0 4z"/></svg>
          www.vitamira-example.com
        </li>
        <li>
          <span class="social-square" aria-hidden="true"></span>
          www.socialpage.example/Vitamira
        </li>
      </ul>
    </div>
  </section>

</main>
</body>
</html>
```